Conference website: Kelvar Civic Forum Meetup 2015

We need a web design to help develop a modern and interactive website for the 2nd Kelvar Civic Meetup which main objective will be to present and discuss real-life Kelvar business initiatives being implemented by entrepreneurs and corporate innovators that are driving sustainable innovation from the bottom up

This is a bi-annual event and will build on the 1st Kelvar Civic Forum Meetup
http://www.kelvarcivicforum.example/summit-2013. It is important that the new website maintain consistency with the 1) the Kelvar Civic Forum Logo (www.kelvarcivicforum.example), 2) the visual identity from the fist event and 3) the organization TQR Logo (www.t7qr.example) -- but the design should be modern, clean, and crisp.

Target Market(s)

Corporations, academics, executives, entrepreneurs, consultants, multilateral organizations, founders, institutions

Industry/Entity Type

Business

Coding

Coded - Design and coding required

Number of Pages Required

5+ page

Font styles to use
Sans Serif

Colors
f68d4d
9bcb3b
3276b5
faa54b
00a88f
0792cd
f37022
9bcb3c
0355a3

Requirements
Must have
• maintain consistency with Kelvar Civic Forum Logo
• dynamic to get the attention
• design modern, clean and crisp
• content should be well linked (e.i. photos and bios liked to the name of speaker on sessions).
• Has to link to a registration system
• Needs to be under the Kelvar Civic Forum domain www.kelvarcivicforum.example
• Preference to URL kelvarcivicforum.example/Summit2015
Nice to have
• different techniques to display menus, photos and bios and description of sessions
• connect somehow with the visual communication developed on last summit in 2013
Should not have
• should not be the same previously
• should not be traditional
• should not be static

```html
<!DOCTYPE html>
<html lang="en">
<head>
<meta charset="utf-8">
<title>Kelvar Civic Forum Meetup 2015</title>
<link rel="stylesheet" href="https://fonts.googleapis.com/css2?family=Lato:wght@300;400;700&display=swap">
<style>
:root{
  --green:#1f8a3c;
  --blue:#0b6fc4;
  --blue-deep:#0355a3;
  --navy:#1d4f9a;
  --grey-band:#e6e8ea;
  --text:#555a60;
  --text-dark:#333;
  --footer:#2f3030;
  --footer-text:#cfd0d0;
  --line:#dcdcdc;
  --white:#fff;
}
*{box-sizing:border-box;margin:0;padding:0}
html,body{width:1200px;height:2540px;overflow:hidden}
body{font-family:"Lato",Arial,sans-serif;color:var(--text);background:var(--white);position:relative}
.section{position:absolute;left:0;width:1200px}

/* top bar */
.topbar{top:0;height:30px;background:var(--green);color:var(--white);font-size:12px;display:flex;align-items:center;justify-content:space-between;padding:0 30px 0 74px}
.social{display:flex;gap:5px}
.social span{width:17px;height:17px;border-radius:50%;background:var(--white);display:block}

/* header */
.header{top:30px;height:136px;background:var(--white)}
.brand{position:absolute;left:74px;top:22px;display:flex;align-items:center;gap:12px}
.brand-mark{width:58px;height:58px;background:var(--navy);display:block}
.brand-name{font-size:24px;font-weight:400;color:var(--navy);line-height:1}
.event-title{position:absolute;left:417px;top:42px;font-size:26px;color:var(--blue);letter-spacing:1px}
.partners{position:absolute;left:728px;top:30px;display:flex;gap:18px;align-items:center}
.partner-badge{width:110px;height:36px;border-radius:18px;background:#e9edf0;display:block}
.lang-tag{position:absolute;left:958px;top:34px;width:50px;height:26px;background:var(--green);clip-path:polygon(22% 0,100% 0,100% 100%,22% 100%,0 50%)}
.lang-flag{position:absolute;left:1034px;top:35px;width:34px;height:24px;background:#2a9a3c}
.main-nav{position:absolute;left:417px;top:92px;display:flex;gap:17px;font-size:13.5px;font-weight:700;color:var(--green);text-transform:uppercase;letter-spacing:.3px}

/* hero */
.hero{top:166px;height:356px}
.hero-photo{position:absolute;left:0;top:0;width:1016px;height:356px;background:linear-gradient(100deg,#3b2a20 0%,#8c5a3a 35%,#c08a5f 55%,#6b4630 80%,#2a1c15 100%)}
.hero-prev{position:absolute;left:76px;top:160px;width:54px;height:54px;background:rgba(60,60,60,.75);display:flex;align-items:center;justify-content:center}
.side-menu{position:absolute;left:1016px;top:0;width:184px;height:356px;background:var(--white);list-style:none}
.side-menu li{height:44.5px;border-bottom:1px solid var(--line);font-size:12.5px;color:var(--text-dark);padding:0 10px;display:flex;align-items:center}
.side-menu li.active{background:var(--green);color:var(--white)}

/* title band */
.title-band{top:522px;height:100px;background:var(--blue);color:var(--white);display:flex;align-items:center;padding-left:88px;font-size:26px}

/* intro */
.intro{top:622px;height:183px;background:var(--grey-band);padding:37px 74px 0;font-size:12px;line-height:1.6;color:#777}
.intro p{margin-bottom:16px;max-width:1060px}
.intro a{color:var(--blue);text-decoration:none}

/* content */
.content{top:805px;height:1016px}
.announcements{position:absolute;left:74px;top:38px;width:236px}
.announcements h2{font-weight:300;font-size:27px;color:var(--text-dark);margin-bottom:16px}
.news-list{list-style:none;border:1px solid var(--line)}
.news-list li{border-bottom:1px solid var(--line);padding:16px 12px 14px}
.news-list li:last-child{border-bottom:0}
.news-title{font-size:13.5px;font-weight:700;color:var(--text-dark);line-height:1.4}
.news-date{font-size:10px;color:#888;margin-top:5px}
.news-list li.active{background:var(--blue)}
.news-list li.active .news-title,.news-list li.active .news-date{color:var(--white)}
.view-more{display:block;text-align:right;margin-top:16px;font-size:13px;font-weight:700;color:var(--blue)}

.about{position:absolute;left:351px;top:38px;width:781px}
.about h2{font-size:32px;font-weight:400;color:var(--green);line-height:1.2;margin-bottom:22px}
.about p{font-size:13px;line-height:23px;margin-bottom:20px;color:var(--text)}
.about .history{margin-top:30px}
.speakers{position:relative;margin-top:30px}
.speakers h2{margin-bottom:0}
.speaker-row{display:flex;justify-content:space-between;padding:0 54px 0 70px;margin-top:14px}
.speaker{width:196px;text-align:center}
.speaker-photo{width:174px;height:174px;border-radius:50%;margin:0 auto;border:3px solid #ddd;background:radial-gradient(circle at 50% 40%,#b88d72 0%,#6f5344 60%,#3d3a3a 100%)}
.speaker-name{font-size:20px;color:var(--text-dark);margin-top:14px}
.speaker-role{font-size:12px;line-height:1.45;color:var(--text);margin-top:4px}
.speaker-link{display:inline-block;margin-top:12px;background:var(--blue-deep);color:var(--white);font-size:10px;padding:4px 14px}
.carousel-arrow{position:absolute;top:126px}
.carousel-arrow.prev{left:0}
.carousel-arrow.next{right:0}

/* banner */
.banner{top:1821px;height:421px;background:linear-gradient(90deg,#0c4aa8 0%,#0a5ec7 50%,#0b6ad0 100%)}
.banner-photo{position:absolute;left:0;top:0;width:640px;height:421px;background:linear-gradient(90deg,#082e6e 0%,#1453b0 60%,rgba(11,106,208,0) 100%)}
.banner-copy{position:absolute;left:643px;top:58px;width:490px;color:var(--white)}
.banner-copy h2{font-size:38px;font-weight:300;line-height:1.15}
.banner-copy h3{font-size:30px;font-weight:300;margin-top:4px}
.banner-copy p{font-size:12.5px;line-height:1.6;margin-top:26px}
.outline-btn{display:inline-block;margin-top:26px;border:2px solid var(--white);color:var(--white);font-size:14px;width:198px;height:42px;line-height:38px;text-align:center}

/* footer */
.footer{top:2242px;height:264px;background:var(--footer);color:var(--footer-text)}
.footer-col{position:absolute;top:46px}
.footer-col h3{font-size:21px;font-weight:400;color:var(--white);margin-bottom:18px}
.footer-col p{font-size:12px;line-height:1.55}
.col-about{left:74px;width:310px}
.col-contact{left:540px;width:250px}
.col-news{left:882px;width:260px}
.col-news p{margin-bottom:14px}
.contact-phone{margin-top:12px}
.footer-social{display:flex;gap:6px;margin-top:12px}
.footer-social span{width:18px;height:18px;border-radius:50%;background:var(--white);display:block}
.copyright{top:2506px;height:34px;background:var(--white);color:#444;font-size:11px;display:flex;align-items:center;justify-content:center}
</style>
</head>
<body>

<div class="section topbar">
  <span>Phone: (555) 014-2290</span>
  <div class="social" aria-label="Social links"><span></span><span></span><span></span><span></span><span></span></div>
</div>

<header class="section header">
  <div class="brand"><span class="brand-mark"></span><span class="brand-name">Kelvar Civic Forum</span></div>
  <div class="event-title">SUMMIT 2015</div>
  <div class="partners"><span class="partner-badge"></span><span class="partner-badge"></span></div>
  <span class="lang-tag"></span>
  <span class="lang-flag"></span>
  <nav class="main-nav"><span>Kelvar Civic Forum</span><span>Knowledge Base</span><span>Sponsors &amp; Partners</span><span>Join Us</span><span>Events</span><span>Contact Us</span></nav>
</header>

<section class="section hero">
  <div class="hero-photo" role="img" aria-label="Close-up photo of an elderly woman, warm earthy tones"></div>
  <div class="hero-prev"><svg width="20" height="30" viewBox="0 0 20 30"><path d="M16 3 L4 15 L16 27" fill="none" stroke="#fff" stroke-width="3"/></svg></div>
  <ul class="side-menu">
    <li class="active">About the Summit</li>
    <li>Sponsors &amp; Partners</li>
    <li>Registration</li>
    <li>Program</li>
    <li>Logistic</li>
    <li>Organizers</li>
    <li>Contact</li>
    <li>Application Forms</li>
  </ul>
</section>

<div class="section title-band">Lifting the Poor Through Business: First International Kelvar Civic Forum Meetup</div>

<section class="section intro">
  <p>New business models and products, innovation ecosystems, sustainability, financial education, and how to bring new opportunities to the world's poorest populations were among the main topics of the first international Kelvar Civic Forum Meetup.</p>
  <p>The event mobilized corporate leaders, non-profits, Kelvar Lab leaders, students, academics, entrepreneurs, community and government representatives, and journalists, on 7 and 8 November, 2013, at the headquarters of Norvale, in Quarrytown, Estavo... <a href="#">Read More</a></p>
</section>

<section class="section content">
  <aside class="announcements">
    <h2>Announcements</h2>
    <ul class="news-list">
      <li class="active"><div class="news-title">FUNDER BRIEFING Verano Highland Sacred Sites of the Calden Ridge, Marvosa Monday June 2 9am to 11am</div><div class="news-date">June 1, 2014</div></li>
      <li><div class="news-title">Registration for 2014 Global Forum on Community Giving now open</div><div class="news-date">May 22, 2014</div></li>
      <li><div class="news-title">Kelvar is offering exciting internships this summer!</div><div class="news-date">May 15, 2014</div></li>
      <li><div class="news-title">Interview with Mara Tellen</div><div class="news-date">April 22, 2014</div></li>
      <li><div class="news-title">2015 Kelvar Summit Call for Sessions</div><div class="news-date">April 16, 2014</div></li>
      <li><div class="news-title">Funders Briefing – Panel Discussion honoring 2014 Halvern Environmental Prize Winner from South America</div><div class="news-date">April 15, 2014</div></li>
      <li><div class="news-title">Rosalind Veyra on Community Giving (Heritage Commons)</div><div class="news-date">April 14, 2014</div></li>
    </ul>
    <a class="view-more">View More</a>
  </aside>

  <article class="about">
    <h2>About the Summit</h2>
    <p>There are many variations of passages of Lorem Ipsum available, but the majority have suffered alteration in some form, by injected humour, or randomised words which don't look even slightly believable. If you are going to use a passage of Lorem Ipsum, you need to be sure there isn't anything embarrassing hidden in the middle of text.</p>
    <p>All the Lorem Ipsum generators on the Internet tend to repeat predefined chunks as necessary, making this the first true generator on the Internet. It uses a dictionary of over 200 Latin words, combined with a handful of model sentence structures, to generate Lorem Ipsum which looks reasonable. The generated Lorem Ipsum is therefore always free from repetition, injected humour, or non-characteristic words etc.</p>
    <h2 class="history">History</h2>
    <p>There are many variations of passages of Lorem Ipsum available, but the majority have suffered alteration in some form, by injected humour, or randomised words which don't look even slightly believable. If you are going to use a passage of Lorem Ipsum, you need to be sure there isn't anything embarrassing hidden in the middle of text.</p>
    <p>All the Lorem Ipsum generators on the Internet tend to repeat predefined chunks as necessary, making this the first true generator on the Internet. It uses a dictionary of over 200 Latin words, combined with a handful of model sentence structures, to generate Lorem Ipsum which looks reasonable. The generated Lorem Ipsum is therefore always free from repetition, injected humour, or non-characteristic words etc.</p>
    <div class="speakers">
      <h2>Speakers</h2>
      <svg class="carousel-arrow prev" width="16" height="30" viewBox="0 0 16 30"><path d="M13 3 L3 15 L13 27" fill="none" stroke="#aaa" stroke-width="2"/></svg>
      <svg class="carousel-arrow next" width="16" height="30" viewBox="0 0 16 30"><path d="M3 3 L13 15 L3 27" fill="none" stroke="#aaa" stroke-width="2"/></svg>
      <div class="speaker-row">
        <div class="speaker"><div class="speaker-photo" role="img" aria-label="Speaker portrait"></div><div class="speaker-name">Loram Ipsum</div><div class="speaker-role">Lorem Ipsum is simply dummy text of the printing and typesetting</div><span class="speaker-link">Read More</span></div>
        <div class="speaker"><div class="speaker-photo" role="img" aria-label="Speaker portrait"></div><div class="speaker-name">Loram Ipsum</div><div class="speaker-role">Lorem Ipsum is simply dummy text of the printing and typesetting</div><span class="speaker-link">Read More</span></div>
        <div class="speaker"><div class="speaker-photo" role="img" aria-label="Speaker portrait"></div><div class="speaker-name">Loram Ipsum</div><div class="speaker-role">Lorem Ipsum is simply dummy text of the printing and typesetting</div><span class="speaker-link">Read More</span></div>
      </div>
    </div>
  </article>
</section>

<section class="section banner">
  <div class="banner-photo" role="img" aria-label="Photo of children bowing their heads, tinted blue"></div>
  <div class="banner-copy">
    <h2>Raising the base of</h2>
    <h3>the pyramid through enterprise</h3>
    <p>Lorem Ipsum is simply dummy text of the printing and typesetting industry. Lorem Ipsum has been the industry's standard dummy text ever since the 1500s, when an unknown printer took a galley of type and scrambled it to make a type specimen book.</p>
    <span class="outline-btn">View More</span>
  </div>
</section>

<footer class="section footer">
  <div class="footer-col col-about">
    <h3>About Us</h3>
    <p>There are many variations of passages of Lorem Ipsum available, but the majority have suffered alteration in some form, by injected humour, or randomised words which don't look even slightly believable. If you are going to use a passage of Lorem Ipsum, you need to be sure there isn't anything embarrassing hidden in the middle of text.</p>
  </div>
  <div class="footer-col col-contact">
    <h3>Contact Us</h3>
    <p>410 Lindenholt Ave.<br>Marrow Bay, NR 20418</p>
    <p class="contact-phone">(555) 014-2290</p>
    <div class="footer-social"><span></span><span></span><span></span><span></span><span></span></div>
  </div>
  <div class="footer-col col-news">
    <h3>Latest News</h3>
    <p>There are many variations of passages of Lorem Ipsum available, but the majority</p>
    <p>There are many variations of passages of Lorem Ipsum available, but the majority</p>
  </div>
</footer>

<div class="section copyright">© Copyright 2012-2014 by kelvarcivicforum.example. All rights reserved.</div>

</body>
</html>
```